I need a box design created for a DNA Fitness Test

I need a modern and sleek box design for a fitness test. The box needs to have our logo on it and should be clean and modern. The Box is 9 Inches Long 3 and 3/4 inches wide, and 2 inches tall. Company logo attached. The company name is cedar vitality.

Target Market(s)

Fitness

Industry/Entity Type

Fitness

Requirements
Must have
• Our logo

```html
<!DOCTYPE html>
<html lang="en">
<head>
<meta charset="utf-8">
<title>Cedar Vitality – Box Dieline</title>
<link rel="stylesheet" href="https://fonts.googleapis.com/css2?family=Barlow:wght@400;500;700&display=swap">
<style>
  :root {
    --page: #ffffff;
    --ink: #111111;
    --line: #2a2a2a;
    --accent-green: #8dd21c;
    --mark-blue: #2a8fd0;
    --helix-green: #a6ec9a;
    --helix-cyan: #9ef0f4;
  }
  * { box-sizing: border-box; margin: 0; padding: 0; }
  html, body { width: 1200px; height: 2400px; overflow: hidden; }
  body {
    background: var(--page);
    font-family: "Barlow", Arial, sans-serif;
    color: var(--ink);
    position: relative;
  }
  .dieline {
    position: absolute;
    left: 193px;
    top: 658px;
    width: 814px;
  }
  .panel {
    position: relative;
    width: 814px;
    border: 1.5px solid var(--line);
    border-bottom: none;
    overflow: hidden;
    background: var(--page);
  }
  .panel--lid { height: 338px; }
  .panel--side { height: 181px; }
  .panel--info { height: 339px; }
  .panel--base { height: 181px; border-bottom: 1.5px solid var(--line); }
  .tuck-flap { display: block; width: 814px; height: 46px; }

  .helix-pattern {
    position: absolute;
    border-radius: 60px;
    background: linear-gradient(135deg, var(--helix-green), var(--helix-cyan) 50%, var(--helix-green));
    opacity: 0.55;
  }

  .brand {
    position: absolute;
    left: 0; right: 0;
    display: flex;
    flex-direction: column;
    align-items: center;
  }
  .brand__dot {
    border-radius: 50%;
    background: var(--mark-blue);
  }
  .brand__name {
    display: flex;
    flex-direction: column;
    align-items: center;
    font-weight: 700;
    color: var(--ink);
    text-transform: uppercase;
    white-space: nowrap;
    line-height: 1;
  }
  .brand__word--main { letter-spacing: 1px; }

  .brand--lid { top: 38px; }
  .brand--lid .brand__dot { width: 110px; height: 110px; margin-bottom: 40px; }
  .brand--lid .brand__word--main { font-size: 62px; }
  .brand--lid .brand__word--sub { font-size: 22px; letter-spacing: 13px; margin-top: 10px; padding-left: 13px; }

  .brand--small { top: 36px; }
  .brand--small .brand__dot { width: 54px; height: 54px; margin-bottom: 14px; }
  .brand--small .brand__word--main { font-size: 28px; }
  .brand--small .brand__word--sub { font-size: 10px; letter-spacing: 6px; margin-top: 3px; padding-left: 6px; }

  .brand--flipped { top: 38px; transform: scaleY(-1); }

  .info__title {
    position: absolute;
    top: 34px; left: 0; right: 0;
    text-align: center;
    font-size: 47px;
    font-weight: 500;
    color: var(--accent-green);
    letter-spacing: 0.5px;
  }
  .info__body {
    position: absolute;
    z-index: 1;
    top: 108px;
    left: 93px;
    width: 630px;
    font-size: 15.4px;
    line-height: 18px;
    color: var(--ink);
    white-space: nowrap;
  }
</style>
</head>
<body>
  <main class="dieline">
    <section class="panel panel--lid">
      <div class="helix-pattern" style="left:567px;top:13px;width:244px;height:143px" role="img" aria-label="Decorative DNA helix pattern in light green and cyan"></div>
      <div class="brand brand--lid">
        <span class="brand__dot"></span>
        <span class="brand__name"><span class="brand__word--main">Cedar</span><span class="brand__word--sub">Vitality</span></span>
      </div>
    </section>

    <section class="panel panel--side">
      <div class="helix-pattern" style="left:6px;top:60px;width:260px;height:118px" role="img" aria-label="Decorative DNA helix pattern in light green and cyan"></div>
      <div class="helix-pattern" style="left:546px;top:8px;width:259px;height:113px" role="img" aria-label="Decorative DNA helix pattern in light green and cyan"></div>
      <div class="brand brand--small">
        <span class="brand__dot"></span>
        <span class="brand__name"><span class="brand__word--main">Cedar</span><span class="brand__word--sub">Vitality</span></span>
      </div>
    </section>

    <section class="panel panel--info">
      <h2 class="info__title">Lorem ipsum</h2>
      <p class="info__body">Lorem ipsum dolor sit amet, consectetuer adipiscing elit, sed diam nonummy nibh euismod<br>tincidunt ut laoreet dolore magna aliquam erat volutpat. Ut wisi enim ad minim veniam, quis<br>nostrud exerci tation ullamcorper suscipit lobortis nisl ut aliquip ex ea commodo consequat.<br>Duis autem vel eum iriure dolor in hendrerit in vulputate velit esse molestie consequat, vel<br>illum dolore eu feugiat nulla facilisis at vero eros et accumsan et iusto odio dignissim qui<br>blandit praesent luptatum zzril delenit augue duis dolore te feugait nulla facilisi.<br>Lorem ipsum dolor sit amet, cons ectetuer adipiscing elit, sed diam nonummy nibh euismod<br>tincidunt ut laoreet dolore magna aliquam erat volutpat. Ut wisi enim ad minim veniam, quis<br>nostrud exerci tation ullamcorper suscipit lobortis nisl ut aliquip ex ea commodo consequat.<br>Lorem ipsum dolor sit amet, consectetuer adipiscing elit, sed diam nonummy nibh euismod<br>tincidunt ut laoreet dolore magna aliquam erat volutpat. Ut wisi enim ad minim veniam, quis</p>
      <div class="helix-pattern" style="left:742px;top:196px;width:62px;height:132px" role="img" aria-label="Decorative DNA helix pattern in light green and cyan"></div>
    </section>

    <section class="panel panel--base">
      <div class="helix-pattern" style="left:6px;top:6px;width:260px;height:118px" role="img" aria-label="Decorative DNA helix pattern in light green and cyan"></div>
      <div class="helix-pattern" style="left:546px;top:59px;width:259px;height:117px" role="img" aria-label="Decorative DNA helix pattern in light green and cyan"></div>
      <div class="brand brand--small brand--flipped">
        <span class="brand__dot"></span>
        <span class="brand__name"><span class="brand__word--main">Cedar</span><span class="brand__word--sub">Vitality</span></span>
      </div>
    </section>

    <svg class="tuck-flap" viewBox="0 0 814 46" aria-hidden="true">
      <polygon points="0.75,0 813.25,0 793,45.25 21,45.25" fill="#ffffff" stroke="#2a2a2a" stroke-width="1.5"/>
    </svg>
  </main>
</body>
</html>
```